I want to revise my business card design and get a more modern and up to date design.

Brolvane Handyman Sevices originated from a family-owned and operated contractor business, performing home renovation, addition, and construction work in the NYC area since 2004. Today, we specialize in reliable and affordable handyman services for residential and commercial clients In 2014, we expanded to northern New Jersey. In 2016, we brought quality home improvement and repair services to new Bucks County, PA, and nearby New Jersey areas.
Target Market(s)
Home owners and business that might be looking for a General contractor, handyman, cleaning services and Home maintenance and property.
Industry/Entity Type
Construction Company
Contact Information for Business Card
I am open to new ideas
Colors
Designer to choose colors to be used in the design.
Look and feel
Each slider illustrates characteristics of the customer's brand and the style your logo design should communicate.

```html
<!DOCTYPE html>
<html lang="en">
<head>
<meta charset="utf-8">
<title>Brolvane Handyman Sevices – Business Card</title>
<link href="https://fonts.googleapis.com/css2?family=Roboto:wght@700&display=swap" rel="stylesheet">
<style>
  :root {
    --stage: #5e4a35;
    --paper: #ffffff;
    --brand-red: #e8202a;
    --ink: #111111;
    --text-dark: #1b1b1b;
    --photo-light: #f1ede8;
    --photo-warm: #e4c58a;
    --photo-tan: #cdb08a;
  }
  * { box-sizing: border-box; margin: 0; padding: 0; }
  html, body {
    width: 1189px; height: 1200px; overflow: hidden;
    background: var(--stage);
    font-family: "Roboto", Arial, sans-serif;
    font-weight: 700;
  }
  .card {
    position: absolute; left: 169px; width: 851px; height: 485px;
    border-radius: 26px; overflow: hidden;
    box-shadow: 0 6px 16px rgba(0,0,0,.45);
  }
  .card--front { top: 112px; background: var(--paper); }
  .card--back { top: 641px; }

  .brand { position: absolute; display: flex; align-items: center; gap: 18px; color: var(--ink); }
  .brand__dot { width: 72px; height: 72px; border-radius: 50%; background: var(--brand-red); flex: none; }
  .brand__name { display: flex; flex-direction: column; line-height: 1; }
  .brand__word { font-size: 78px; letter-spacing: -1px; }
  .brand__tag { font-size: 15px; letter-spacing: 4.2px; margin-top: 8px; }
  .card--front .brand { left: 50%; top: 78px; transform: translateX(-50%); }

  .name-band {
    position: absolute; left: 0; top: 272px; width: 100%; height: 51px;
    background: var(--brand-red); color: #fff;
    font-size: 35px; text-align: center; line-height: 51px;
  }
  .contact-panel {
    position: absolute; left: 0; top: 323px; width: 100%; height: 162px;
    background: var(--ink); color: #fff; text-align: center;
  }
  .contact-panel__phone { font-size: 26px; margin-top: 12px; }
  .contact-panel__email { font-size: 26px; margin-top: 6px; }
  .services {
    display: flex; justify-content: center; align-items: center; gap: 12px;
    margin-top: 20px; font-size: 26px;
  }
  .services__mark { width: 14px; height: 14px; background: var(--brand-red); transform: rotate(45deg); }

  .back-photo {
    position: absolute; inset: 0;
    background:
      radial-gradient(ellipse 45% 60% at 78% 62%, var(--photo-warm) 0%, rgba(228,197,138,.5) 45%, rgba(228,197,138,0) 80%),
      linear-gradient(90deg, var(--photo-light) 0%, #ebe6df 45%, var(--photo-tan) 100%);
  }
  .card--back .brand { left: 55px; top: 95px; }
  .card--back .brand__word { font-size: 82px; }
  .features { position: absolute; left: 62px; top: 325px; list-style: none; }
  .features__item {
    display: flex; align-items: center; gap: 18px;
    font-size: 25px; color: var(--text-dark); height: 48px;
  }
  .features__item::before {
    content: ""; width: 24px; height: 24px; border-radius: 50%; background: var(--brand-red); flex: none;
  }
</style>
</head>
<body>
  <section class="card card--front">
    <div class="brand">
      <span class="brand__dot"></span>
      <div class="brand__name">
        <span class="brand__word">Brolvane</span>
        <span class="brand__tag">HANDYMAN SEVICES</span>
      </div>
    </div>
    <div class="name-band">Tiago Marques</div>
    <div class="contact-panel">
      <p class="contact-panel__phone">(215) 555-0148</p>
      <p class="contact-panel__email">brolvanehandyman@mail.com</p>
      <div class="services">
        <span class="services__mark"></span><span>REPAIR</span>
        <span class="services__mark"></span><span>IMPROVE</span>
        <span class="services__mark"></span><span>MAINTAIN</span>
        <span class="services__mark"></span><span>REMODEL</span>
      </div>
    </div>
  </section>

  <section class="card card--back">
    <div class="back-photo" role="img" aria-label="Photo of a handyman in a tool belt holding a pipe wrench and a yellow hard hat, in front of a bright blurred interior"></div>
    <div class="brand">
      <span class="brand__dot"></span>
      <div class="brand__name">
        <span class="brand__word">Brolvane</span>
        <span class="brand__tag">HANDYMAN SEVICES</span>
      </div>
    </div>
    <ul class="features">
      <li class="features__item">Handyman and tasks by General contractor</li>
      <li class="features__item">Property maintenance</li>
      <li class="features__item">Cleaning and handyman services</li>
    </ul>
  </section>
</body>
</html>
```